Looking to update current business card

We have a two sided card currently that needs a fresher, newer look. I like the fact it has two sides with a list of products/services we offer on the back side but the overall front look is lackluster. Our logo will stay the same.. I just want someone to bring some new life into the business card.

I like cards that have rounded corners but not sure if there's enough room?

Attached is our current biz card design and logo.

Target Market(s)

business customers

Industry/Entity Type

Business

Contact Information for Business Card

see above

```html
<!DOCTYPE html>
<html lang="en">
<head>
<meta charset="utf-8">
<title>Corvane Secure – Business Card</title>
<link href="https://fonts.googleapis.com/css2?family=Open+Sans:wght@400;600;700&display=swap" rel="stylesheet">
<style>
  :root {
    --bg: #e9e7e4;
    --card: #ffffff;
    --card-shade: #f0f0f1;
    --brand-blue: #3b6291;
    --brand-orange: #f08a4b;
    --text-dark: #333a42;
    --text-grey: #4a4f55;
  }
  * { box-sizing: border-box; margin: 0; padding: 0; }
  html, body {
    width: 1200px; height: 900px; overflow: hidden;
    background: var(--bg);
    font-family: "Open Sans", Arial, sans-serif;
  }
  .canvas {
    width: 1200px; height: 900px;
    display: flex; align-items: center; justify-content: center;
  }
  .business-card {
    position: relative;
    width: 1000px; height: 572px;
    border-radius: 60px;
    overflow: hidden;
    background: radial-gradient(ellipse at 45% 40%, var(--card) 0%, var(--card) 45%, var(--card-shade) 100%);
    box-shadow: 0 12px 30px rgba(0,0,0,0.18);
  }
  .card-band {
    position: absolute; inset: 0;
    width: 100%; height: 100%;
  }
  .band-blue { fill: var(--brand-blue); }
  .band-orange { fill: none; stroke: var(--brand-orange); stroke-width: 14; }

  .brand {
    position: absolute; left: 80px; top: 160px;
    display: flex; align-items: center; gap: 12px;
  }
  .brand-dot {
    width: 18px; height: 18px; border-radius: 50%;
    background: var(--brand-orange);
  }
  .brand-name {
    font-size: 34px; font-weight: 700; color: var(--brand-blue);
    letter-spacing: 0.3px;
  }

  .address {
    position: absolute; left: 80px; top: 255px;
    font-size: 24px; line-height: 37px; color: var(--text-dark);
  }

  .contact-list {
    position: absolute; left: 80px; top: 375px;
    list-style: none;
    font-size: 22px; line-height: 36px; color: var(--text-dark);
  }
  .contact-list li { display: flex; align-items: center; gap: 14px; }
  .contact-icon { width: 20px; height: 20px; fill: var(--brand-blue); flex: none; }

  .person {
    position: absolute; left: 500px; top: 135px;
  }
  .person-name {
    font-size: 26px; font-weight: 700; color: var(--brand-blue);
    letter-spacing: 0.5px; text-transform: uppercase;
  }
  .person-title {
    font-size: 21px; color: var(--text-grey); margin-top: 2px;
  }
</style>
</head>
<body>
<main class="canvas">
  <section class="business-card" aria-label="Business card front">
    <svg class="card-band" viewBox="0 0 1000 572" aria-hidden="true">
      <path class="band-orange" d="M725,0 A520,520 0 0 1 885,215"/>
      <path class="band-blue" d="M760,0 A520,520 0 0 1 840,572 L1000,572 L1000,0 Z"/>
    </svg>

    <div class="brand">
      <span class="brand-dot"></span>
      <span class="brand-name">Corvane Secure</span>
    </div>

    <p class="address">214, 9th floor, Ridge Tower<br>Elm Street</p>

    <ul class="contact-list">
      <li>
        <svg class="contact-icon" viewBox="0 0 24 24"><path d="M6.6 10.8a15.1 15.1 0 0 0 6.6 6.6l2.2-2.2a1 1 0 0 1 1-.25 11.4 11.4 0 0 0 3.6.57 1 1 0 0 1 1 1V20a1 1 0 0 1-1 1A17 17 0 0 1 3 4a1 1 0 0 1 1-1h3.5a1 1 0 0 1 1 1c0 1.25.2 2.45.57 3.57a1 1 0 0 1-.25 1z"/></svg>
        <span>045 778 2310</span>
      </li>
      <li>
        <svg class="contact-icon" viewBox="0 0 24 24"><path d="M2 5h20v14H2z"/><path d="M3 6l9 7 9-7" fill="none" stroke="#fff" stroke-width="1.6"/></svg>
        <span>hello@corvanesecure.com</span>
      </li>
      <li>
        <svg class="contact-icon" viewBox="0 0 24 24"><circle cx="12" cy="12" r="10"/><path d="M2 12h20M12 2c3 3 3 17 0 20M12 2c-3 3-3 17 0 20M4 7h16M4 17h16" fill="none" stroke="#fff" stroke-width="1.3"/></svg>
        <span>www.corvanesecure.com</span>
      </li>
    </ul>

    <div class="person">
      <h1 class="person-name">Martin Hale</h1>
      <p class="person-title">Managing Director</p>
    </div>
  </section>
</main>
</body>
</html>
```